Pull Up Banner - Recruitment Company

We would like a design for a pull up banner.

For context: we are a recruitment business. We specialise in helping people in healthcare industry to find jobs in Australia.

I have come up with several ideas and text for the banner. Feel free to use the following as you see appropriate:

- Our logo (see attached)
- 'Healthcare Recruitment Agency'
- Some sort of imagine / cartoon of medical professionals (ie. doctor, nurse, physiotherapist, speech pathologist). A cartoon is more friendly than committing to a photo
- 'Empowering your next career move'
- 'Discover tailored opportunities based on your career preferences'
- Dot points (allied health, nursing, medical imaging)
- Contact info at the bottom including our website (www.quellstaffing.com.au, our Instagram handle @quellstaffing, Mobile: XXXX XXX XXX. The title section for contact information could be 'Get in touch:'

Feel free to submit a couple of designs and we can merge aspects that look good on your designs and find the perfect fit.
Thank you
Updates

Hello,

Thank you for your initial submissions to this project. I appreciate the time you've invested.

After reviewing the first attempt, I'd like to share some feedback and initial observations:

- Professionalism and engagement: Is the overall appearance of the banner professional? It's crucial that we have a high-quality design as this will represent our business.

- Image selection: The image (whether cartoon or real people) appears quite generic. Please consider submitting the banner with a few different photos in the middle for us to choose from. Ensure the image is a good fit and not simply a generic stock photo.

- Contact section: Kindly remove the phone number; we no longer wish to include it on the banner. Instead, please include our website (www.quellstaffing.com.au) and Instagram handle (@quellstaffing).

- Color scheme: White, black, and red/pink are preferred, or alternatively, blue. However, please avoid incorporating too many different colors as it may detract from the professional appearance.

We will be printing the design on a banner and require it to look professional and engaging.

Thank you once again for your submissions. I hope the feedback provided above is helpful.

Warm regards,

Target Market(s)

Allied Health Australia

Font styles to use
Serif

Colors
0054AA
0677BA
7BADD7
CADEEF
E8F1F8
0094D4
00A9DD
6FCCEA
C7EBF8
E9F6FB
EB3D1F
EC4F4E
F09395
F8D3D4
FCEDEE

```html
<!DOCTYPE html>
<html lang="en">
<head>
<meta charset="utf-8">
<title>Quell Staffing – Pull Up Banners</title>
<link rel="stylesheet" href="https://fonts.googleapis.com/css2?family=Playfair+Display:wght@700;800&family=Roboto:wght@400;500;700&display=swap">
<style>
  :root {
    --page-bg: #d9dcd6;
    --teal: #9edcdb;
    --teal-light: #c4ecea;
    --pink: #e8207f;
    --red: #eb3d1f;
    --ink: #1a1a1a;
    --ice: #e8f1f8;
    --white: #ffffff;
    --blue: #0094d4;
    --blue-pale: #c7ebf8;
    --serif: "Playfair Display", Georgia, serif;
    --sans: "Roboto", Arial, sans-serif;
  }
  * { box-sizing: border-box; margin: 0; padding: 0; }
  html, body { width: 1200px; height: 1047px; overflow: hidden; }
  body { background: var(--page-bg); font-family: var(--sans); color: var(--ink); position: relative; }

  .banner { position: absolute; top: 66px; width: 380px; height: 914px; overflow: hidden; box-shadow: 0 8px 24px rgba(0,0,0,.18); }
  .banner--pink { left: 110px; background: var(--ice); }
  .banner--blue { left: 710px; background: var(--ice); }

  .brand { position: absolute; top: 24px; left: 22px; font-family: var(--sans); font-weight: 700; font-size: 18px; letter-spacing: 3px; color: var(--ink); z-index: 2; }

  /* Pink banner */
  .hero { position: absolute; top: 0; left: 0; width: 100%; height: 330px; background: linear-gradient(180deg, var(--teal-light), var(--teal)); }
  .hero__photo { position: absolute; left: 0; top: 78px; width: 175px; height: 252px; background: linear-gradient(180deg, #b7e4e2 0%, #e9d7cc 45%, #f4f6f7 75%, #e6eef2 100%); }
  .hero__title { position: absolute; left: 168px; top: 112px; font-family: var(--serif); font-weight: 700; font-size: 29px; line-height: 1.18; color: var(--ink); }
  .hero__title .flag { display: inline-block; background: var(--red); color: var(--white); padding: 0 6px; margin-left: -6px; }
  .hero__tag { position: absolute; left: 168px; top: 224px; font-size: 10.5px; font-weight: 500; color: var(--ink); }
  .band { position: absolute; top: 330px; left: 0; width: 100%; height: 44px; background: var(--pink); }
  .offer { position: absolute; top: 404px; left: 20px; width: 350px; font-family: var(--serif); font-weight: 700; font-size: 30px; line-height: 1.22; }
  .offer em { font-style: normal; color: var(--pink); }
  .specialties { position: absolute; top: 590px; left: 20px; list-style: none; font-size: 21px; line-height: 1.6; }
  .specialties li::before { content: "*"; color: var(--pink); font-weight: 700; margin-right: 8px; font-size: 24px; }
  .cartoon { position: absolute; top: 560px; left: 262px; width: 88px; height: 190px; border-radius: 40px 40px 6px 6px; background: linear-gradient(180deg, #f2e3da, #ffffff 35%, #5c7fa8 70%, #3b5a80); }
  .contact--pink { position: absolute; bottom: 0; left: 0; width: 100%; height: 168px; background: var(--pink); text-align: center; padding-top: 34px; }
  .contact--pink::before { content: ""; position: absolute; top: 0; left: 178px; border-left: 12px solid transparent; border-right: 12px solid transparent; border-top: 12px solid var(--ice); }
  .contact__head { font-size: 23px; font-weight: 500; margin-bottom: 14px; }
  .contact__line { font-size: 14px; font-weight: 500; margin-bottom: 16px; }

  /* Blue banner */
  .team { position: absolute; top: 0; left: 0; }
  .banner--blue .brand { top: 26px; }
  .headline { position: absolute; top: 392px; width: 100%; text-align: center; font-family: var(--serif); font-weight: 800; font-size: 40px; line-height: 1.2; }
  .headline .flag { display: inline-block; background: var(--red); color: var(--white); padding: 0 10px; margin: 4px 0; }
  .tagline { position: absolute; top: 570px; width: 100%; text-align: center; font-size: 19px; font-weight: 500; line-height: 1.3; text-transform: uppercase; }
  .rule { position: absolute; top: 640px; left: 0; width: 100%; height: 5px; display: flex; }
  .rule span:first-child { flex: 0 0 60%; background: var(--red); }
  .rule span:last-child { flex: 1; background: var(--ink); }
  .offer--blue { position: absolute; top: 664px; left: 22px; width: 200px; text-align: center; font-size: 18px; font-weight: 500; line-height: 1.35; }
  .specialties--blue { position: absolute; top: 668px; left: 228px; list-style: none; font-size: 12px; line-height: 1.75; }
  .specialties--blue li::before { content: "*"; color: var(--red); font-weight: 700; margin-right: 4px; }
  .contact--blue { position: absolute; bottom: 0; left: 0; width: 100%; height: 150px; background: var(--white); text-align: center; padding-top: 22px; }
  .contact--blue .contact__head { font-size: 22px; margin-bottom: 10px; }
  .contact--blue .contact__line { font-size: 13px; margin-bottom: 10px; display: flex; align-items: center; justify-content: center; gap: 6px; }
  .dot { width: 12px; height: 12px; border-radius: 50%; background: var(--red); display: inline-block; }
  .stripe { position: absolute; bottom: 0; left: 0; width: 100%; height: 14px; display: flex; }
  .stripe span:first-child { flex: 0 0 45%; background: var(--ink); }
  .stripe span:last-child { flex: 1; background: var(--red); }
</style>
</head>
<body>

<section class="banner banner--pink">
  <div class="hero">
    <div class="hero__photo" role="img" aria-label="Photo of a smiling doctor with a stethoscope pointing to the headline"></div>
    <h1 class="hero__title">Healthcare<br><span class="flag">Recruitment</span><br>Agency</h1>
    <p class="hero__tag">Empowering your next career move.</p>
  </div>
  <div class="brand">QUELL STAFFING</div>
  <div class="band"></div>
  <p class="offer">Discover tailored opportunities based on <em>your career</em> preferences.</p>
  <ul class="specialties">
    <li>Allied Health</li>
    <li>Nursing</li>
    <li>Medical Imaging</li>
  </ul>
  <div class="cartoon" role="img" aria-label="Cartoon illustration of a healthcare professional in a white coat with arms crossed"></div>
  <div class="contact--pink">
    <p class="contact__head">Get in touch:</p>
    <p class="contact__line">www.quellstaffing.com.au</p>
    <p class="contact__line">@quellstaffing</p>
  </div>
</section>

<section class="banner banner--blue">
  <svg class="team" width="380" height="380" viewBox="0 0 380 380" role="img" aria-label="Group photo of smiling doctors and nurses in scrubs and white coats">
    <defs>
      <linearGradient id="teamTone" x1="0" y1="0" x2="0" y2="1">
        <stop offset="0" stop-color="#f4f7f9"/>
        <stop offset=".4" stop-color="#e3d3c8"/>
        <stop offset=".75" stop-color="#9ec3e2"/>
        <stop offset="1" stop-color="#e9eef2"/>
      </linearGradient>
    </defs>
    <path d="M0 0 H380 V292 Q230 372 0 300 Z" fill="url(#teamTone)"/>
    <path d="M0 312 Q220 386 380 298" fill="none" stroke="var(--blue)" stroke-width="9"/>
  </svg>
  <div class="brand">QUELL STAFFING</div>
  <h1 class="headline">Healthcare<br><span class="flag">Recruitment</span><br>Agency</h1>
  <p class="tagline">Empowering your next<br>career move.</p>
  <div class="rule"><span></span><span></span></div>
  <p class="offer--blue">Discover tailored opportunities based on your career preferences.</p>
  <ul class="specialties--blue">
    <li>Allied Health</li>
    <li>Nursing</li>
    <li>Medical Imaging</li>
  </ul>
  <div class="contact--blue">
    <p class="contact__head">Get in touch:</p>
    <p class="contact__line">www.quellstaffing.com.au</p>
    <p class="contact__line"><span class="dot"></span>@quellstaffing</p>
    <div class="stripe"><span></span><span></span></div>
  </div>
</section>

</body>
</html>
```